Music portal needs a sleek mobile app design

We need an innovative, cutting edge design for our mobile app for www.loftaroundsound.com . LOFTAROUND Music is a platform that lets independent musicians upload and share their music for free. Music lovers can discover new music too.

If you visit the website, you'll get an idea of our brand colors and theme. im attaching the logo and our new discover page layout. We use "din Next LT pro" as our brand font.

We are looking for an app optimized for iOS, but can be used on Android and windows too.

Im looking for a design that flows and navigates with user intuition and is sleek, flat style in nature and has Similar apps are tunewharf, riffpantry and beatorchard.

Here are some ideas we like, but please dont copy. Come up with something similar in 'feel'

https://www.portfoliarc.net/gallery/B-TUNE-IT-Music-application/4412983

https://sketchvault.com/shots/2290518-Music-App

The most important pages/ screens for us are:
- The discover screen
- The login and sign up screens
- The splash screen
- The track player screen
- The use profile page screen
Updates

It seems no design has come close to what I was looking for so I will be requesting a refund and withdrawing this project. Thanks for your effort

Target Market(s)

music, music app, tunewharf, loftaround music, music app design

Colors
f78f20
ffcf3e
ffffff
000000

Requirements
Must have
• a sleek easy to use navigation- please create an account on loftaroundsound.com to see how the site works.
Nice to have
• Sleek screen to screen transitions
Should not have
• no 3d designs. Flat design only

```html
<!DOCTYPE html>
<html lang="en">
<head>
<meta charset="utf-8">
<title>Welcome – Sign In</title>
<link rel="stylesheet" href="https://fonts.googleapis.com/css2?family=Montserrat:wght@400;500;600&display=swap">
<style>
  :root {
    --orange: #f78f20;
    --yellow: #ffcf3e;
    --white: #ffffff;
    --black: #000000;
    --haze-mid: #6f675b;
    --haze-dark: #3d3a33;
    --meadow: #4a4a32;
  }
  * { box-sizing: border-box; margin: 0; padding: 0; }
  html, body {
    width: 677px;
    height: 1200px;
    overflow: hidden;
    background: var(--black);
  }
  body { font-family: "Montserrat", "Helvetica Neue", Arial, sans-serif; }
  .welcome-screen {
    position: relative;
    width: 677px;
    height: 1200px;
    overflow: hidden;
    color: var(--white);
  }
  .hero-backdrop {
    position: absolute;
    inset: 0;
    background:
      radial-gradient(ellipse 420px 360px at 520px 330px, rgba(255, 236, 190, 0.55), rgba(255, 236, 190, 0) 70%),
      linear-gradient(180deg, var(--haze-dark) 0%, var(--haze-mid) 30%, #85796a 52%, #5d5846 72%, var(--meadow) 100%);
  }
  .hero-backdrop::after {
    content: "";
    position: absolute;
    inset: 0;
    background: linear-gradient(180deg, rgba(0,0,0,0.15) 0%, rgba(0,0,0,0.05) 45%, rgba(0,0,0,0.35) 100%);
  }
  .brand-mark {
    position: absolute;
    left: 232px;
    top: 264px;
    width: 212px;
    height: 194px;
    background: var(--black);
    border: 4px solid var(--orange);
    display: flex;
    align-items: center;
    justify-content: center;
  }
  .brand-name {
    font-weight: 600;
    font-size: 26px;
    letter-spacing: 1px;
    color: var(--orange);
  }
  .intro {
    position: absolute;
    left: 38px;
    top: 651px;
    width: 620px;
  }
  .intro-title {
    font-weight: 500;
    font-size: 36px;
    line-height: 38px;
    letter-spacing: 3.5px;
    white-space: nowrap;
  }
  .intro-tagline {
    font-weight: 400;
    font-size: 22px;
    line-height: 27px;
    letter-spacing: 0.5px;
    color: var(--orange);
  }
  .pager {
    display: flex;
    gap: 9px;
    margin-top: 16px;
  }
  .pager-dot {
    width: 11px;
    height: 11px;
    border-radius: 50%;
    border: 2px solid var(--white);
  }
  .pager-dot.is-active { background: var(--white); }
  .signup-prompt {
    position: absolute;
    top: 994px;
    left: 0;
    width: 100%;
    text-align: center;
    font-size: 22px;
    line-height: 28px;
    letter-spacing: 0.5px;
    font-weight: 400;
  }
  .signup-link { color: var(--orange); text-decoration: none; }
  .sign-in-button {
    position: absolute;
    left: 32px;
    top: 1094px;
    width: 613px;
    height: 72px;
    border: none;
    border-radius: 4px;
    background: var(--orange);
    color: var(--white);
    font-family: "Montserrat", "Helvetica Neue", Arial, sans-serif;
    font-weight: 600;
    font-size: 24px;
    letter-spacing: 2px;
  }
</style>
</head>
<body>
  <main class="welcome-screen">
    <div class="hero-backdrop" role="img" aria-label="Sunlit meadow photograph of a person with long hair in a flowing dress, backlit by warm sun"></div>

    <div class="brand-mark">
      <span class="brand-name">FERNLOW</span>
    </div>

    <section class="intro">
      <h1 class="intro-title">Share and discover new<br>sounds.</h1>
      <p class="intro-tagline">Forever Fre and Unlimited.</p>
      <div class="pager" aria-hidden="true">
        <span class="pager-dot"></span>
        <span class="pager-dot is-active"></span>
        <span class="pager-dot"></span>
        <span class="pager-dot"></span>
      </div>
    </section>

    <p class="signup-prompt">Don't have an account? <a class="signup-link" href="#">Sign Up</a></p>

    <button class="sign-in-button" type="button">SIGN IN</button>
  </main>
</body>
</html>
```